Desk Allies Business Card

Contact Information for Business Card

Janne Voutilainen
Managing Director

3/47 Brindle Street Larkmoor ACT 2999

Tel: +61 02 6257 3140
Mob: +61 0427 315 846

Email: janne@deskallies.com.au
Web: www.deskallies.com.au

Colors

Designer to choose colors to be used in the design.

Requirements
Must have
• Logo, Name, Title, Address, Telephone, Mobile, Email Address and Website
• "Desk Ally International Pty Ltd"

```html
<!DOCTYPE html>
<html lang="en">
<head>
<meta charset="utf-8">
<title>Desk Allies Business Card</title>
<link rel="stylesheet" href="https://fonts.googleapis.com/css2?family=Montserrat:wght@500;700&family=Roboto:wght@400&display=swap">
<style>
  :root {
    --brand-blue: #2271ad;
    --ink: #4a4a4a;
    --ink-soft: #777777;
    --paper: #f7f7f7;
    --backdrop: #e9e9e9;
    --rule: #9a9a9a;
    --white: #ffffff;
  }
  * { margin: 0; padding: 0; box-sizing: border-box; }
  html, body { width: 1200px; height: 1189px; overflow: hidden; }
  body {
    background: var(--backdrop);
    font-family: "Roboto", Arial, sans-serif;
    display: flex;
    align-items: center;
    justify-content: center;
    gap: 44px;
  }
  .card {
    position: relative;
    width: 525px;
    height: 300px;
    box-shadow: 0 6px 18px rgba(0,0,0,0.12);
  }
  .card--front { background: var(--paper); }
  .card--back { background: var(--brand-blue); color: var(--white); }

  .wordmark {
    display: flex;
    align-items: center;
    gap: 12px;
    font-family: "Montserrat", Arial, sans-serif;
    font-weight: 700;
    letter-spacing: 0.02em;
    text-transform: uppercase;
  }
  .wordmark__dot { border-radius: 50%; flex: none; }

  .card--front .wordmark {
    position: absolute; left: 30px; top: 26px;
    color: var(--brand-blue); font-size: 24px;
  }
  .card--front .wordmark__dot { width: 34px; height: 34px; background: var(--brand-blue); }

  .person { position: absolute; left: 30px; top: 84px; }
  .person__name {
    font-family: "Montserrat", Arial, sans-serif;
    font-weight: 700; font-size: 17px; color: var(--brand-blue);
  }
  .person__title { font-size: 12.5px; color: var(--ink-soft); margin-top: 2px; }

  .divider {
    position: absolute; left: 30px; right: 30px; top: 136px;
    border-top: 1px solid var(--rule);
  }

  .contact { position: absolute; left: 30px; top: 150px; list-style: none; }
  .contact__item {
    display: flex; align-items: center; gap: 9px;
    font-size: 12.5px; color: var(--ink); line-height: 21px;
  }
  .contact__icon { width: 12px; height: 12px; flex: none; }

  .address {
    position: absolute; right: 30px; bottom: 26px;
    text-align: right; font-size: 12.5px; color: var(--ink); line-height: 18px;
  }

  .card--back .wordmark {
    position: absolute; left: 0; right: 0; top: 100px;
    justify-content: center; font-size: 32px; color: var(--white);
  }
  .card--back .wordmark__dot { width: 44px; height: 44px; background: var(--white); }
  .company {
    position: absolute; left: 0; right: 0; top: 180px;
    text-align: center; font-size: 14px; font-weight: 400; letter-spacing: 0.02em;
  }
</style>
</head>
<body>

<section class="card card--front" aria-label="Business card front">
  <div class="wordmark"><span class="wordmark__dot"></span>Desk Allies</div>

  <div class="person">
    <p class="person__name">Janne Voutilainen</p>
    <p class="person__title">Managing Director</p>
  </div>

  <div class="divider"></div>

  <ul class="contact">
    <li class="contact__item">
      <svg class="contact__icon" viewBox="0 0 12 12" fill="none" stroke="#2271ad" stroke-width="1.3"><path d="M3 1.5 L4.5 4 L3.5 5 Q4.5 7.5 7 8.5 L8 7.5 L10.5 9 L9.5 10.5 Q4 10 1.5 3 Z"/></svg>
      +61 02 6257 3140
    </li>
    <li class="contact__item">
      <svg class="contact__icon" viewBox="0 0 12 12" fill="none" stroke="#2271ad" stroke-width="1.2"><rect x="3" y="1" width="6" height="10" rx="1"/><line x1="5" y1="9.3" x2="7" y2="9.3"/></svg>
      +61 0427 315 846
    </li>
    <li class="contact__item">
      <svg class="contact__icon" viewBox="0 0 12 12" fill="none" stroke="#2271ad" stroke-width="1.2"><rect x="1" y="2.5" width="10" height="7"/><path d="M1 2.5 L6 6.5 L11 2.5"/></svg>
      janne@deskallies.com.au
    </li>
    <li class="contact__item">
      <svg class="contact__icon" viewBox="0 0 12 12" fill="none" stroke="#2271ad" stroke-width="1.1"><circle cx="6" cy="6" r="5"/><ellipse cx="6" cy="6" rx="2.2" ry="5"/><line x1="1" y1="6" x2="11" y2="6"/></svg>
      www.deskallies.com.au
    </li>
  </ul>

  <p class="address">3/47 Brindle Street<br>Larkmoor ACT 2999</p>
</section>

<section class="card card--back" aria-label="Business card back">
  <div class="wordmark"><span class="wordmark__dot"></span>Desk Allies</div>
  <p class="company">Desk Ally International Pty Ltd</p>
</section>

</body>
</html>
```